Web Design Project

Psychotherapy and Counselling Practice needs a landing page web design.

My business "Larkspur Advisory" specialises in the treatment of Anxiety and Depression with a holistic approach, endeavouring to unlock the key that holds us to ransom in a life that is imbalanced, frustrating, and ultimately of our own making due to our own perceptions and behaviours.

There is much that impacts us which we cannot change, but we are always in control of how we think, and how we frame our experiences.....learning to challenge those thoughts and behaviours that are destructive and disempowering opens up a world of joyful possibility. Life is about making choices, learn to make wiser and healthier choices.......

Larkspur Advisory has a client base of individual clients but will seek to expand to offer services to the Corporate world by offering an adjunct to employers for established "Wellness Programs".

Larkspur Advisory is a highly professional, ethically bound business, with the needs of the client at the forefront of all we do.

Larkspur Advisory wishes to avoid the usual "jargon driven" psychobabble offered on many counselling web pages. It aims to be stylishly presented, clean in look and with as few "words" as possible and a largely white background (faster loading and more powerful impact of what is stated), those words contained in the webpage should be meaningful, persuasive and have an impact simply at glance. Larkspur does not want , or expect, those prospective clients in need of support , to be reading through volumes of industry driven cliches.

At this point Larkspur is just looking for a high quality landing page. However in time this will likely expand to include other sections such as case studies, video content etc.

Target Market(s)

Those in need of emotional support, suffering mental health issues, and those simply wanting to become self aware supported by a mindful therapist.

Industry/Entity Type

Industry

Requirements
Must have
• The design must incorporate the Larkspur logo and colour schemes found on the attached files.

```html
<!DOCTYPE html>
<html lang="en">
<head>
<meta charset="utf-8">
<title>Larkspur Advisory</title>
<link href="https://fonts.googleapis.com/css2?family=Open+Sans:wght@300;400;600;700&family=Raleway:wght@300;400;500&display=swap" rel="stylesheet">
<style>
  :root{
    --green:#8cc63f;
    --sky-top:#1f6fc0;
    --sky-mid:#5fa3de;
    --sky-bottom:#b9dcf3;
    --ink:#3d3d3d;
    --muted:#6e7a63;
    --line:#d7d7d7;
    --footer:#3b3b3b;
    --footer-text:#bdbdbd;
    --white:#ffffff;
  }
  *{box-sizing:border-box;margin:0;padding:0}
  html,body{width:820px;height:1200px;overflow:hidden;background:var(--white)}
  body{font-family:"Open Sans",Arial,sans-serif;color:var(--ink);position:relative}

  .site-header{height:104px;position:relative}
  .brand{position:absolute;left:34px;top:40px;display:flex;align-items:center;gap:8px}
  .brand-dot{width:12px;height:12px;border-radius:50%;background:var(--green)}
  .brand-name{font-size:20px;font-weight:600;color:var(--green);letter-spacing:1px;text-transform:uppercase}
  .main-nav{position:absolute;left:310px;top:54px;display:flex;gap:30px}
  .main-nav a{font-size:11px;color:#7a7a7a;text-decoration:none;letter-spacing:.5px;text-transform:uppercase}
  .social{position:absolute;right:92px;top:16px;display:flex;gap:12px}
  .social span{width:22px;height:22px;border-radius:50%;background:var(--green);display:block}

  .hero{position:absolute;top:104px;left:0;width:820px;height:330px;
    background:linear-gradient(180deg,var(--sky-top) 0%,var(--sky-mid) 55%,var(--sky-bottom) 100%)}
  .hero-tagline{position:absolute;left:70px;top:226px;color:var(--white);font-size:24px;font-weight:300;line-height:1.3;font-family:"Raleway",sans-serif}
  .hero-tagline em{font-style:normal;font-weight:500}

  .mission{position:absolute;top:460px;left:0;width:820px;height:210px;text-align:center}
  .mission h1{font-family:"Raleway",sans-serif;font-weight:400;font-size:27px;line-height:1.25;text-transform:uppercase;color:var(--ink);padding-top:36px}
  .mission p{width:600px;margin:22px auto 0;font-size:16px;line-height:1.5;color:var(--muted)}

  .people{position:absolute;top:682px;left:0;width:820px;height:222px;display:grid;grid-template-columns:repeat(8,1fr);grid-template-rows:repeat(3,1fr);gap:2px}
  .people span{display:block}
  .t1{background:#c9a68a}.t2{background:#d8c0a8}.t3{background:#b58a6a}.t4{background:#e1ccb6}
  .t5{background:#9e7a5e}.t6{background:#cdb39a}.t7{background:#e6d6c4}.t8{background:#b9987c}
  .cta{position:absolute;top:774px;left:50%;transform:translateX(-50%);background:var(--green);color:var(--white);font-size:20px;font-weight:600;letter-spacing:.5px;padding:10px 32px;text-transform:uppercase;white-space:nowrap}

  .testimonial{position:absolute;top:922px;left:0;width:820px;height:120px}
  .client-photo{position:absolute;left:82px;top:6px;width:104px;height:104px;border-radius:50%;background:radial-gradient(circle at 50% 40%,#d9c3ad,#7b6656);border:3px solid var(--white);box-shadow:0 0 0 1px var(--line)}
  .quote-box{position:absolute;left:232px;top:0;width:540px;height:116px;border:1px solid var(--line);border-radius:4px;padding:16px 20px 0 60px}
  .quote-box::before{content:"";position:absolute;left:-9px;top:48px;width:16px;height:16px;background:var(--white);border-left:1px solid var(--line);border-bottom:1px solid var(--line);transform:rotate(45deg)}
  .quote-mark{position:absolute;left:18px;top:4px;font-size:46px;color:#cfcfcf;font-family:Georgia,serif}
  .quote-box p{font-size:11.5px;line-height:1.5;color:#777}
  .quote-box cite{display:block;margin-top:10px;font-style:normal;font-size:11px;color:#555}
  .quote-box cite b{font-weight:600}

  .site-footer{position:absolute;top:1066px;left:0;width:820px;height:134px;background:var(--footer);padding:16px 60px 0;display:grid;grid-template-columns:190px 300px 1fr;color:var(--footer-text)}
  .site-footer h3{font-size:14px;font-weight:600;color:var(--white);margin-bottom:8px}
  .site-footer ul{list-style:none}
  .site-footer li{font-size:10px;line-height:1.6}
  .tweet{font-size:10px;line-height:1.45;margin-bottom:4px}
  .contact-row{font-size:10px;line-height:1.6;display:flex}
  .contact-row span:first-child{width:60px}
</style>
</head>
<body>
  <header class="site-header">
    <div class="brand"><span class="brand-dot"></span><span class="brand-name">Larkspur</span></div>
    <nav class="main-nav">
      <a href="#">Home</a><a href="#">About</a><a href="#">Services</a><a href="#">Testimonials</a><a href="#">Contact</a>
    </nav>
    <div class="social"><span></span><span></span><span></span></div>
  </header>

  <section class="hero" role="img" aria-label="Photo of a woman leaping joyfully against a blue sky, trailing a green scarf">
    <p class="hero-tagline">Life is too short<br>to live an <em>unhappy</em> life...</p>
  </section>

  <section class="mission">
    <h1>Our mission is to change this world<br>to be a better place</h1>
    <p>Research shows that more than half of the people around the world are not satisfied and happy with their life, we try to help people to find their happiness and make their life worth living.</p>
  </section>

  <section class="people" role="img" aria-label="Grid of portrait photos of smiling people of all ages">
    <span class="t1"></span><span class="t2"></span><span class="t3"></span><span class="t4"></span><span class="t5"></span><span class="t6"></span><span class="t7"></span><span class="t8"></span>
    <span class="t4"></span><span class="t7"></span><span class="t1"></span><span class="t6"></span><span class="t2"></span><span class="t8"></span><span class="t3"></span><span class="t5"></span>
    <span class="t6"></span><span class="t3"></span><span class="t8"></span><span class="t2"></span><span class="t7"></span><span class="t1"></span><span class="t5"></span><span class="t4"></span>
  </section>
  <a class="cta">Be happy now!</a>

  <section class="testimonial">
    <div class="client-photo" role="img" aria-label="Portrait photo of the client giving the testimonial"></div>
    <blockquote class="quote-box">
      <span class="quote-mark">&ldquo;</span>
      <p>These sessions changed how I see my days. Every meeting was calm, clear and kind, and I left each one with a simple step I could take forward.</p>
      <cite><b>Maren,</b> Director of Northfield Co</cite>
    </blockquote>
  </section>

  <footer class="site-footer">
    <div>
      <h3>Useful Links</h3>
      <ul><li>About us</li><li>Products</li><li>Services</li><li>Support</li><li>Contact us</li></ul>
    </div>
    <div>
      <h3>Latest Tweets</h3>
      <p class="tweet">@larkspur Small daily choices shape how we feel. Pause, breathe and notice one good thing today.</p>
      <p class="tweet">New blog post: framing stressful moments in a calmer way.<br>12 minutes ago</p>
    </div>
    <div>
      <h3>Contact Us</h3>
      <div class="contact-row"><span>Phone</span><span>+61 2 5550 1842</span></div>
      <div class="contact-row"><span>Fax</span><span>+61 2 5550 1843</span></div>
      <div class="contact-row"><span>E-mail</span><span>hello@larkspur.example</span></div>
      <div class="contact-row"><span>Address</span><span>14 Harbour Lane, Suite 3,<br>City, Country</span></div>
    </div>
  </footer>
</body>
</html>
```